A3 Poster Design for BUSINESS COACHING services

A3 Poster design for business coaching - we want it to be visual - minimal words. Needs to contain:
- our logo (uploaded)
- the words BUSINESS COACHING - Business or a Hobby? Talk to us today about our business coaching services to take your business to the next level
- and some graphics (open to ideas of something representative of coaching/working together/ improving business profits/success)
The poster will be physically in our business premises and will be more a cue for existing clients to ask us about a service they may not know we offer and so why it doesn't need to be informational

Target Market(s)

Small to Medium Business Owners

Industry/Entity Type

Small Business

Requirements
Must have
• Needs to contain:
• - our logo (uploaded)
• - the words BUSINESS COACHING - Business or a Hobby? Talk to us today about our business coaching services to take your business to the next level
• - and some graphics (open to ideas of something representative of coaching/working together/ improving business profits/success)

```html
<!DOCTYPE html>
<html lang="en">
<head>
<meta charset="utf-8">
<title>Business Coaching Poster</title>
<link rel="stylesheet" href="https://fonts.googleapis.com/css2?family=Short+Stack&family=Oswald:wght@500&family=Playfair+Display:ital@1&family=Roboto:wght@700&display=swap">
<style>
  :root {
    --page-bg: #d9dcda;
    --board-edge: #7f9a8b;
    --board-mid: #9cb3a6;
    --board-glow: #e6efe9;
    --ink: #2a2d2b;
    --rule: #f2f5f3;
    --accent: #8dc63f;
    --illustration-tone: #7b9283;
  }
  * { margin: 0; padding: 0; box-sizing: border-box; }
  html, body { width: 960px; height: 1200px; overflow: hidden; }
  body { background: var(--page-bg); position: relative; }

  .poster {
    position: absolute;
    left: 180px; top: 20px;
    width: 600px; height: 1160px;
    background:
      radial-gradient(ellipse 300px 280px at 50% 84%, var(--board-glow) 0%, rgba(230,239,233,0.55) 40%, rgba(156,179,166,0) 80%),
      radial-gradient(ellipse at 50% 40%, var(--board-mid) 0%, var(--board-edge) 100%);
    color: var(--ink);
    text-align: center;
  }

  .title {
    position: absolute; left: 0; right: 0; top: 160px;
    font-family: "Short Stack", cursive;
    font-weight: 400;
    font-size: 70px;
    line-height: 86px;
    letter-spacing: 1px;
  }

  .tagline {
    position: absolute; left: 110px; right: 110px; top: 376px;
    display: flex; align-items: center; gap: 14px;
    font-family: "Playfair Display", serif;
    font-style: italic;
    font-size: 18px;
  }
  .tagline::before, .tagline::after {
    content: ""; flex: 1; height: 2px; background: var(--rule);
  }

  .message {
    position: absolute; left: 40px; right: 40px; top: 410px;
    font-family: "Oswald", sans-serif;
    font-weight: 500;
    font-size: 20px;
    line-height: 29px;
    letter-spacing: 0.6px;
    text-transform: uppercase;
  }

  .coaching-journey {
    position: absolute; left: 85px; top: 522px;
    width: 440px; height: 230px;
    display: flex; align-items: center; justify-content: space-between;
  }
  .journey-step {
    width: 116px; height: 220px;
    border-radius: 58px 58px 14px 14px;
    background: var(--illustration-tone);
  }
  .journey-step--thinking { height: 230px; align-self: flex-start; }
  .journey-arrow { width: 36px; height: 20px; margin-top: 70px; }
  .journey-arrow path { fill: none; stroke: var(--ink); stroke-width: 2.5; stroke-linecap: round; stroke-linejoin: round; }

  .brand {
    position: absolute; left: 0; right: 0; top: 950px;
    display: flex; justify-content: center; align-items: center; gap: 14px;
    font-family: "Roboto", sans-serif;
    font-weight: 700;
    font-size: 36px;
    color: var(--ink);
  }
  .brand-dot {
    width: 22px; height: 22px; border-radius: 50%; background: var(--accent);
  }
</style>
</head>
<body>
  <main class="poster">
    <h1 class="title">BUSINESS<br>COACHING</h1>
    <p class="tagline">Business or a Hobby?</p>
    <p class="message">Talk to us today about our business coaching<br>services to take your business to the next level</p>
    <div class="coaching-journey">
      <div class="journey-step" role="img" aria-label="Line drawing of a head in profile with a question mark"></div>
      <svg class="journey-arrow" viewBox="0 0 36 20" aria-hidden="true"><path d="M2 14 L32 8 M25 3 L32 8 L26 14"/></svg>
      <div class="journey-step journey-step--thinking" role="img" aria-label="Line drawing of a head in profile with turning gears inside"></div>
      <svg class="journey-arrow" viewBox="0 0 36 20" aria-hidden="true"><path d="M2 6 L32 12 M26 6 L32 12 L25 17"/></svg>
      <div class="journey-step" role="img" aria-label="Line drawing of a head in profile with an exclamation mark"></div>
    </div>
    <div class="brand"><span class="brand-dot"></span><span class="brand-name">Crestline Advisory</span></div>
  </main>
</body>
</html>
```